Law Firm Website, easily updated by User

We are a regional Labor and Employment Law Firm with a tired outdated website. We are looking for a clean easy to use website that will allow us to easily update information and articles in house. Our current website can be found at www.quillbrookcounsel.com

Industry/Entity Type

Labor

Number of Pages Required

5+ page

Colors
0655a3

Requirements
Must have
• Content easily updated by user
Nice to have
• crisp clean pages
Should not have
• stock pictures

```html
<!DOCTYPE html>
<html lang="en">
<head>
<meta charset="utf-8">
<title>Quillbrook Counsel, P.C.</title>
<link rel="stylesheet" href="https://fonts.googleapis.com/css2?family=Tinos:wght@400;700&display=swap">
<style>
:root{
  --brand:#0655a3;
  --brand-deep:#1a4a8c;
  --section-blue:#1c4a8e;
  --ink:#222;
  --black:#000;
  --bar:#111;
  --white:#fff;
  --hero-top:#8a8a8a;
  --hero-bottom:#4e4e4e;
}
*{box-sizing:border-box;margin:0;padding:0}
html,body{width:892px;height:1200px;overflow:hidden;background:var(--white)}
body{font-family:"Tinos","Times New Roman",serif;color:var(--ink);position:relative}
.abs{position:absolute}

.brand{left:120px;top:14px;display:flex;align-items:center;gap:8px}
.brand-square{width:30px;height:30px;background:var(--brand-deep)}
.brand-name{font-size:24px;color:var(--brand-deep);line-height:1}
.brand-tag{left:120px;top:50px;font-size:7px;letter-spacing:.2px;color:var(--ink);border-top:1px solid var(--brand-deep);padding-top:2px;width:245px}

.consult-banner{left:494px;top:0;width:288px;height:54px}
.consult-text{left:494px;top:2px;width:288px;text-align:center;color:var(--white);font-weight:700}
.consult-text .small{font-size:15px;display:block}
.consult-text .big{font-size:23px;display:block;line-height:1.1}

.main-nav{left:0;top:85px;width:892px;height:45px;background:var(--bar);display:flex;padding-left:121px}
.main-nav a{color:#bbb;text-decoration:none;font-size:22px;line-height:45px;padding:0 12px}
.main-nav a.active{background:var(--white);color:var(--brand-deep);height:45px}

.hero{left:0;top:130px;width:892px;height:422px;background:linear-gradient(var(--hero-top),var(--hero-bottom))}
.hero-arrow{top:527px;width:44px;height:44px;border-radius:50%;background:var(--white);box-shadow:0 1px 4px rgba(0,0,0,.25)}
.hero-arrow.prev{left:85px}
.hero-arrow.next{left:764px}

.services{left:112px;top:447px;width:674px;height:208px;background:var(--white);box-shadow:0 2px 6px rgba(0,0,0,.2)}
.services-title{left:122px;top:455px;font-size:20px;color:var(--brand-deep)}
.service{top:494px;height:138px;border:1px solid #777;padding:6px 9px;background:var(--white)}
.service h3{font-size:22px;color:var(--brand-deep);line-height:1.05;font-weight:700}
.service p{font-size:16px;line-height:1.5;margin-top:2px}

.emblem{left:433px;top:656px;width:28px;height:40px;background:var(--brand-deep)}
.welcome-title{left:0;top:704px;width:892px;text-align:center;font-size:23px;font-weight:700;color:var(--brand-deep)}
.welcome-text{left:118px;top:738px;width:656px;text-align:center;font-size:16px;line-height:1.5}

.feature-band{left:0;top:842px;width:892px;height:261px;background:var(--section-blue)}
.feature-photo{left:108px;top:862px;width:325px;height:106px;background:linear-gradient(90deg,#6a3a1f,#b9784a 45%,#3d2418)}
.feature-title{left:106px;top:975px;font-size:23px;font-weight:700;color:var(--white)}
.feature-text{left:106px;top:1005px;width:320px;font-size:9.5px;line-height:1.45;color:var(--white)}
.btn-read{left:108px;top:1058px;width:124px;height:34px;background:var(--white);color:var(--brand-deep);font-size:17px;font-weight:700;text-align:center;line-height:34px}

.news-title{left:597px;top:860px;width:187px;font-size:23px;font-weight:700;color:var(--white);border-bottom:1px solid var(--white);padding-left:2px;padding-bottom:4px}
.news-item{left:589px;width:200px;color:var(--white)}
.news-date{position:absolute;left:0;width:37px;height:34px;background:#2b2b2b;border:1px solid #aaa;font-size:9px;font-weight:700;text-align:center;line-height:1.15;padding-top:5px}
.news-body{position:absolute;left:64px;width:130px}
.news-body h4{font-size:13px;font-weight:700;margin-bottom:4px}
.news-body p{font-size:9.5px;line-height:1.3}
.news-rule{left:585px;top:982px;width:205px;border-top:1px dotted var(--white)}
.news-more{left:660px;top:1075px;font-size:15px;font-weight:700;color:var(--white);display:flex;align-items:center;gap:6px}

.site-footer{left:0;top:1103px;width:892px;height:97px;background:var(--black);color:var(--white)}
.footer-legal{left:111px;top:1122px;font-size:9.5px;font-weight:700;color:var(--white);line-height:2.6}
.footer-call{left:520px;top:1116px;width:265px;text-align:center;color:var(--white);font-weight:700}
.footer-call .small{display:block;font-size:19px}
.footer-call .big{display:block;font-size:28px;margin-top:6px}
</style>
</head>
<body>

<div class="abs brand"><span class="brand-square"></span><span class="brand-name">Quillbrook Counsel, P.C.</span></div>
<div class="abs brand-tag">EMPLOYMENT COUNSELING, LITIGATION, LABOR &amp; BENEFITS LAW</div>

<svg class="abs consult-banner" viewBox="0 0 288 54" aria-hidden="true"><polygon points="0,0 288,0 270,54 20,54 0,34" fill="var(--brand-deep)"/></svg>
<div class="abs consult-text"><span class="small">For a Free Consultation</span><span class="big">Call (555) 204-3318</span></div>

<nav class="abs main-nav">
  <a class="active" href="#">Home</a><a href="#">Attorneys</a><a href="#">Practice Areas</a><a href="#">News</a><a href="#">Employers</a><a href="#">Contact</a>
</nav>

<div class="abs hero" role="img" aria-label="Team photo of the firm's three attorneys in business attire"></div>

<div class="abs hero-arrow prev"><svg width="44" height="44" viewBox="0 0 44 44"><polyline points="25,14 16,22 25,30" fill="none" stroke="#444" stroke-width="4"/></svg></div>
<div class="abs hero-arrow next"><svg width="44" height="44" viewBox="0 0 44 44"><polyline points="19,14 28,22 19,30" fill="none" stroke="#444" stroke-width="4"/></svg></div>

<section class="abs services"></section>
<div class="abs services-title">Counseling and Advising Clients Exclusively on Laws of the Workplace</div>
<div class="abs service" style="left:144px;width:177px"><h3>Employment<br>Law</h3><p>Lorem Ipsum is simply dummy text of the printing and typesetting</p></div>
<div class="abs service" style="left:353px;width:190px"><h3>ERISA<br>Law</h3><p>Lorem Ipsum is simply dummy text of the printing and typesetting</p></div>
<div class="abs service" style="left:561px;width:190px"><h3>Civil<br>Litigation</h3><p>Lorem Ipsum is simply dummy text of the printing and typesetting</p></div>

<div class="abs emblem"></div>
<h2 class="abs welcome-title">WELCOME TO OUR SITE</h2>
<p class="abs welcome-text">Lorem Ipsum is simply dummy text of the printing and typesetting industry. Lorem Ipsum has been the industry's standard dummy text ever since the 1500s, when an unknown printer took a galley of type and scrambled it to make a type specimen book. It has survived not only five centuries, but also the leap into electronic typesetting, remaining essentially</p>

<section class="abs feature-band"></section>
<div class="abs feature-photo" role="img" aria-label="Photo of a judge's gavel and scales of justice on a wooden desk"></div>
<h3 class="abs feature-title">LOREM IPSUM</h3>
<p class="abs feature-text">IS SIMPLY DUMMY TEXT OF THE PRINTING AND TYPESETTING INDUSTRY. LOREM IPSUM HAS &nbsp;IS SIMPLY DUMMY TEXT OF THE PRINTING AND TYPESETTING INDUSTRY. LOREM IPSUM HAS</p>
<div class="abs btn-read">READ MORE</div>

<h3 class="abs news-title">Latest News</h3>
<div class="abs news-item" style="top:905px">
  <div class="news-date" style="top:23px">19 MAY<br>2015</div>
  <div class="news-body"><h4>LOREM IPSUM</h4><p>IS SIMPLY DUMMY TEXT OF THE PRINTING AND TYPESETTING INDUSTRY. LOREM IPSUM HAS</p></div>
</div>
<div class="abs news-rule"></div>
<div class="abs news-item" style="top:992px">
  <div class="news-date" style="top:22px">19 MAY<br>2015</div>
  <div class="news-body"><h4>LOREM IPSUM</h4><p>IS SIMPLY DUMMY TEXT OF THE PRINTING AND TYPESETTING INDUSTRY. LOREM IPSUM HAS</p></div>
</div>
<div class="abs news-more">READ MORE <svg width="18" height="12" viewBox="0 0 18 12"><polyline points="2,1 7,6 2,11" fill="none" stroke="#fff" stroke-width="2.5"/><polyline points="10,1 15,6 10,11" fill="none" stroke="#fff" stroke-width="2.5"/></svg></div>

<footer class="abs site-footer"></footer>
<div class="abs footer-legal">Copyright © 2013. All Rights Reserved. Quillbrook Counsel, P.C.<br>Privacy Policy | Disclaimer</div>
<div class="abs footer-call"><span class="small">For a Free Consultation</span><span class="big">Call (555) 204-3318</span></div>

</body>
</html>
```